Re-style home page - eye-catching and unique design for social commerce website

We need a new concept design for Trondix's home page.
We don't want to make huge changes but creating a more professional and eye-catching style.

We need to look very serious like a professional services company and in the same time to look like a social network for e-commerce.

Our logo is very captive and you can use to creating something of harmonious.

This is a re-style and I'm excepted to see unique and fresh design like Glimmora.
Updates

Target Market(s)

e-commerce and social

Industry/Entity Type

Social

Number of Pages Required

1 page

Font styles to use
Serif
Sans Serif

Requirements
Must have
• An eye-catching result.
• Search bar with logo and Login How it works and business
• The slogan with login and signup.
• Footer links.
Nice to have
• I would like to open the home page and see only two clear ways:
• -Consumer
• --Search
• --The slogan
• --Login and Signup
• --How it works
• -Business
• --Go to Business area
• Background: City, Shopping.
Should not have
• Scrollbar style!

```html
<!DOCTYPE html>
<html lang="en">
<head>
<meta charset="utf-8">
<title>Trondix – Shop Directly From Your Profile</title>
<link href="https://fonts.googleapis.com/css2?family=Cabin:wght@400;500;600&display=swap" rel="stylesheet">
<style>
  :root {
    --black: #000000;
    --nav-text: #c9b58a;
    --footer-text: #b8b8b8;
    --panel: rgba(20, 20, 20, 0.82);
    --field: #5a5a5a;
    --field-line: #7a7a7a;
    --field-text: #e6e6e6;
    --gold: #c9a21f;
    --gold-dark: #a8861a;
    --blue: #2f4f9e;
    --blue-dark: #23407f;
    --white: #ffffff;
    --muted: #d8d8d8;
    --search-bg: #2a2a2a;
    --search-btn: #4a4a4a;
  }
  * { box-sizing: border-box; margin: 0; padding: 0; }
  html, body { width: 1200px; height: 675px; overflow: hidden; background: var(--black); }
  body { position: relative; font-family: "Cabin", sans-serif; color: var(--white); }

  .hero-photo {
    position: absolute; left: 0; top: 54px; width: 1200px; height: 590px;
    background:
      radial-gradient(ellipse at 20% 40%, rgba(220,200,190,0.55), transparent 55%),
      radial-gradient(ellipse at 82% 45%, rgba(120,95,80,0.6), transparent 55%),
      linear-gradient(90deg, #8c8580 0%, #b7a89c 30%, #7d6a66 50%, #a89b93 70%, #d8d2cc 100%);
  }

  .top-bar { position: absolute; left: 0; top: 0; width: 1200px; height: 54px; background: var(--black); }
  .search {
    position: absolute; left: 225px; top: 18px; width: 268px; height: 25px;
    background: var(--search-bg); border-radius: 6px; overflow: hidden;
  }
  .search-input { position: absolute; left: 14px; top: 6px; font-size: 11px; color: var(--muted); }
  .search-button {
    position: absolute; right: 0; top: 0; width: 29px; height: 25px; background: var(--search-btn);
    display: flex; align-items: center; justify-content: center;
  }
  .main-nav {
    position: absolute; right: 232px; top: 20px; font-size: 13px; color: var(--nav-text);
    display: flex; gap: 10px;
  }
  .main-nav .sep { color: #6c6c6c; }

  .brand {
    position: absolute; left: 527px; top: 0; width: 146px; height: 143px; background: var(--black);
    border-radius: 0 0 10px 10px; display: flex; flex-direction: column; align-items: center; justify-content: center; gap: 12px;
  }
  .brand-mark { width: 34px; height: 34px; background: var(--gold); }
  .brand-name { font-size: 27px; font-weight: 400; color: var(--white); }

  .login-panel {
    position: absolute; left: 375px; top: 216px; width: 450px; height: 428px;
    background: var(--panel); border-radius: 8px 8px 0 0;
  }
  .login-title { position: absolute; top: 42px; width: 100%; text-align: center; font-size: 28px; font-weight: 400; color: #e8e8e8; }
  .fields {
    position: absolute; left: 85px; top: 86px; width: 280px; height: 82px;
    background: var(--field); border-radius: 5px; border: 1px solid #6d6d6d;
  }
  .field { position: absolute; left: 0; width: 100%; height: 41px; display: flex; align-items: center; padding-left: 20px; gap: 12px; font-size: 13px; color: var(--field-text); letter-spacing: 0.5px; }
  .field-email { top: 0; border-bottom: 1px solid var(--field-line); }
  .field-password { top: 41px; }
  .btn { position: absolute; left: 85px; width: 280px; border-radius: 5px; display: flex; align-items: center; justify-content: center; font-weight: 500; color: var(--white); }
  .btn-signin { top: 179px; height: 40px; background: linear-gradient(var(--gold), var(--gold-dark)); font-size: 19px; }
  .slogan-divider { position: absolute; left: 88px; top: 283px; width: 274px; display: flex; align-items: center; gap: 8px; font-size: 12px; font-weight: 500; color: var(--white); }
  .slogan-divider .rule { flex: 1; height: 1px; background: #8a8a8a; }
  .btn-social { top: 306px; height: 39px; background: linear-gradient(var(--blue), var(--blue-dark)); font-size: 17px; justify-content: flex-start; }
  .social-square { width: 38px; height: 39px; background: #3d5fb0; border-radius: 5px 0 0 5px; margin-right: 30px; }
  .panel-links { position: absolute; left: 85px; top: 353px; width: 280px; display: flex; justify-content: space-between; font-size: 11px; color: var(--white); }
  .privacy-note { position: absolute; top: 377px; width: 100%; text-align: center; font-size: 9px; color: var(--muted); text-decoration: underline; }

  .footer { position: absolute; left: 0; top: 643px; width: 1200px; height: 32px; background: var(--black); display: flex; justify-content: center; align-items: center; gap: 14px; font-size: 13px; color: var(--footer-text); }
</style>
</head>
<body>
  <div class="hero-photo" role="img" aria-label="Photo of three smiling women walking through a city street carrying shopping bags"></div>

  <header class="top-bar">
    <div class="search">
      <span class="search-input">eg. smartphone, clothes, clean services, shoes</span>
      <span class="search-button">
        <svg width="16" height="16" viewBox="0 0 16 16"><circle cx="6.5" cy="6.5" r="4.8" fill="none" stroke="#fff" stroke-width="2"/><line x1="10" y1="10" x2="14.5" y2="14.5" stroke="#fff" stroke-width="2.4" stroke-linecap="round"/></svg>
      </span>
    </div>
    <nav class="main-nav">
      <span>Login</span><span class="sep">/</span><span>How it work</span><span class="sep">/</span><span>Business</span>
    </nav>
  </header>

  <div class="brand">
    <span class="brand-mark"></span>
    <span class="brand-name">Trondix</span>
  </div>

  <section class="login-panel">
    <h1 class="login-title">Shop Directly From Your Profile</h1>
    <div class="fields">
      <div class="field field-email">
        <svg width="24" height="17" viewBox="0 0 24 17"><rect x="1" y="1" width="22" height="15" fill="none" stroke="#e0e0e0" stroke-width="1.5"/><polyline points="1,1 12,10 23,1" fill="none" stroke="#e0e0e0" stroke-width="1.5"/></svg>
        <span>email Address</span>
      </div>
      <div class="field field-password">
        <svg width="24" height="22" viewBox="0 0 24 22"><path d="M8 9 V6 a4 4 0 0 1 8 0 V9" fill="none" stroke="#e0e0e0" stroke-width="1.6"/><rect x="6.5" y="9" width="11" height="12" rx="5" fill="none" stroke="#e0e0e0" stroke-width="1.6"/><circle cx="12" cy="15" r="1.5" fill="#e0e0e0"/></svg>
        <span>•••••••••••</span>
      </div>
    </div>
    <div class="btn btn-signin">Sign in</div>
    <div class="slogan-divider"><span class="rule"></span><span>SAVE YOUR TIME. LIVE BETTER</span><span class="rule"></span></div>
    <div class="btn btn-social"><span class="social-square"></span>Sign in with Connectly</div>
    <div class="panel-links"><span>Forgot Password?</span><span>New here? Sign Up</span></div>
    <p class="privacy-note">We take your privacy seriously and will take all measures to protect your personal information</p>
  </section>

  <footer class="footer">
    <span>About us</span><span>Blog</span><span>Business</span><span>Jobs</span><span>Privacy</span><span>FAQ</span><span>Contacts</span>
  </footer>
</body>
</html>
```